Crestwave Glow LED - E- Commerce site

We need a website designed for an LED Billboard company that sells:
1) LED Billboards (Sales & Rental)
2) LED Gas Station lights
3) Truss Systems (Sales & Rental)
4) Sound Systems (Sales & Rental)

Attached are websites that sell similar products as Crestwave Glow LED. Target market is for business, property managers and event coordinators.
This site will need to be an e-commerce site where customers can purchase the product directly from the site. What I'm looking for is a design layout to start.

Conceptual Web Designs:
http://198.51.100.47:8087/index.html
http://www.vomilux-example.com/
http://www.tonarvoxaudio-example.com/
http://www.pelmoraboard-example.com/

Attached is the logo of the company: Please note that the new spelling of the logo is "Crestwave Glow LED" using domain " CrestwaveGlowLED.com

Industry/Entity Type

Gas Station

Number of Pages Required

5+ page

Requirements
Must have
• 1) E-Commerce - Customers will need to be able to order product from the site.
• 2) Customers will also have the option to rent the product as well.
Nice to have
• I like the image of the attached website, that has a video clip loop
• http://www.pelmoraboard-example.com/

```html
<!DOCTYPE html>
<html lang="en">
<head>
<meta charset="utf-8">
<title>Crestwave Glow LED – Home</title>
<link href="https://fonts.googleapis.com/css2?family=Lato:wght@300;400;700;900&display=swap" rel="stylesheet">
<style>
:root{
  --yellow:#f6c21c;
  --yellow-deep:#e2ac12;
  --pink:#e0306d;
  --black:#000;
  --ink:#222;
  --dark-btn:#3b3b3b;
  --grey:#666;
  --line:#d9d9d9;
  --page:#f3f3f3;
  --white:#fff;
}
*{box-sizing:border-box;margin:0;padding:0}
html,body{width:1200px;height:2394px;overflow:hidden}
body{position:relative;background:var(--page);font-family:"Lato",Arial,sans-serif;color:var(--ink)}
.abs{position:absolute}

/* top utility bar */
.utility-bar{left:0;top:0;width:1200px;height:29px;background:var(--yellow);display:flex;justify-content:flex-end;align-items:center;padding-right:95px}
.utility-bar span{font-size:12px;color:#3a2b00;padding:0 11px;border-left:1px solid rgba(0,0,0,.15);display:flex;align-items:center;gap:5px}
.utility-bar span:first-child{border-left:none}
.utility-bar i{display:inline-block;width:8px;height:8px;background:#3a2b00;border-radius:2px}

/* header */
.site-header{left:0;top:29px;width:1200px;height:97px;background:var(--black)}
.brand{left:144px;top:60px;display:flex;align-items:center;gap:10px;color:var(--white);font-size:17px;font-weight:700}
.brand-dot{width:30px;height:30px;border-radius:50%;background:var(--yellow)}
.main-nav{left:330px;top:68px;display:flex;align-items:center}
.main-nav a{color:var(--white);font-size:14.5px;text-decoration:none;padding:0 15px;border-left:1px solid var(--pink);line-height:14px}
.main-nav a:first-child{border-left:none;color:var(--yellow);font-weight:700}
.cart{left:943px;top:59px;width:151px;height:35px;background:var(--white);border-radius:3px;display:flex;align-items:center;overflow:hidden}
.cart-icon{width:32px;height:35px;background:var(--yellow);display:flex;align-items:center;justify-content:center}
.cart-label{font-size:13px;padding-left:13px;color:#111}
.cart-label small{font-size:10px;color:#555}

/* hero */
.hero{left:0;top:126px;width:1200px;height:417px;background:
  radial-gradient(ellipse 260px 200px at 600px 230px,rgba(200,30,40,.75),transparent 70%),
  radial-gradient(ellipse 220px 260px at 1120px 150px,rgba(60,90,170,.6),transparent 70%),
  radial-gradient(ellipse 200px 300px at 60px 250px,rgba(180,80,30,.55),transparent 70%),
  linear-gradient(180deg,#8a8f96 0%,#5c5f66 40%,#3a3536 75%,#5a2a2a 100%)}
.hero-play{left:553px;top:272px}
.hero-title{left:0;top:472px;width:1200px;text-align:center;color:var(--white);font-size:37px;font-weight:300;letter-spacing:.3px}

/* how it works */
.how-band{left:0;top:543px;width:1200px;height:95px;background:var(--black)}
.how-tab{left:0;top:543px;width:265px;height:95px;background:var(--yellow);clip-path:polygon(0 0,236px 0,265px 47px,236px 95px,0 95px)}
.how-title{left:90px;top:562px;font-size:21px;color:#111}
.how-sub{left:91px;top:594px;font-size:13px;color:#111}
.step{top:560px;display:flex;gap:16px}
.step-icon{width:40px;height:44px;background:var(--yellow);border-radius:4px;display:flex;align-items:center;justify-content:center;flex-shrink:0}
.step h4{color:var(--white);font-size:15px;font-weight:700;margin-top:2px}
.step p{color:#ddd;font-size:12px;margin-top:5px;line-height:17px}

/* section heads */
.section-title{left:0;width:1200px;text-align:center;font-size:25px;font-weight:400;color:#111;letter-spacing:.3px}
.section-title em{font-style:normal;color:var(--pink);font-weight:700}
.title-rule{height:1px;background:#bbb}
.pager{display:flex;gap:3px}
.pager b{width:16px;height:16px;background:#aaa;display:flex;align-items:center;justify-content:center}
.section-lead{left:0;width:1200px;text-align:center;font-size:12px;font-style:italic;color:#333}

/* categories */
.category{top:792px;width:243px;height:134px;border-radius:4px;color:var(--white);text-align:center;font-size:17px;box-shadow:0 2px 4px rgba(0,0,0,.3)}
.category .name{position:absolute;top:28px;left:0;right:0}
.category .mode{position:absolute;top:80px;left:0;right:0;font-size:16px}

/* panels */
.panel{left:91px;width:1018px;background:var(--white);border:1px solid #e3e3e3;border-radius:6px}

/* product cards */
.product{width:232px;height:335px;background:var(--white);border:1px solid #cfcfcf;border-radius:3px;overflow:hidden}
.product .thumb{position:absolute;left:1px;top:1px;width:228px;height:238px}
.product .more{position:absolute;left:0;top:202px;width:230px;height:42px;background:var(--yellow);display:flex;align-items:center;gap:8px;padding-left:12px;font-size:20px;color:#222}
.product .more i{width:26px;height:26px;border-radius:50%;background:var(--pink);color:var(--white);font-style:normal;font-size:15px;font-weight:700;display:flex;align-items:center;justify-content:center}
.product .label{position:absolute;left:14px;top:253px;width:204px;font-size:15px;color:#333;padding-bottom:9px;border-bottom:1px dashed #bbb}
.product .actions{position:absolute;left:8px;top:290px;display:flex;gap:4px}
.btn{width:105px;height:42px;display:flex;align-items:center;justify-content:center;color:var(--white);font-size:16px}
.btn-buy{background:var(--pink)}
.btn-rent{background:var(--dark-btn)}

/* perks band */
.perks{left:91px;top:1475px;width:1018px;height:76px;background:var(--yellow-deep);border-radius:3px}
.perk{top:1490px;display:flex;gap:12px;align-items:center}
.perk h5{font-size:14px;font-weight:900;color:#1a1a1a}
.perk p{font-size:12px;color:#3a2b00;margin-top:2px}
.perk-active{left:408px;top:1468px;width:338px;height:90px;background:var(--yellow);box-shadow:0 8px 10px -6px rgba(0,0,0,.35)}

/* tabs */
.tabs{left:427px;top:1623px;display:flex}
.tab{width:176px;height:36px;border:2px solid #ccc;border-bottom:none;display:flex;align-items:center;justify-content:center;font-size:19px;background:var(--white)}
.tab-active{color:var(--pink)}

/* footer */
.footer{left:0;top:2131px;width:1200px;height:218px;background:var(--black)}
.foot-title{color:var(--white);font-size:18px;font-weight:400}
.quick-links{left:98px;top:2154px;color:var(--white)}
.quick-links ul{list-style:none;margin-top:20px}
.quick-links li{font-size:13px;line-height:25.5px;padding-left:14px;position:relative}
.quick-links li::before{content:"";position:absolute;left:0;top:10px;border-left:5px solid var(--pink);border-top:3px solid transparent;border-bottom:3px solid transparent}
.foot-divider{width:1px;background:#333;top:2155px;height:170px}
.map{left:342px;top:2204px;width:204px;height:108px;background:linear-gradient(135deg,#cfe0c8 0%,#e9e4d4 50%,#a9c8e6 100%);border:2px solid #ddd}
.contact{left:570px;top:2204px;font-size:12px;line-height:19px;color:var(--white)}
.contact .row{display:flex;gap:8px;margin-bottom:9px}
.contact .row svg{flex-shrink:0;margin-top:3px}
.foot-brand{left:850px;top:2150px;width:280px;height:178px;display:flex;align-items:center;justify-content:center;gap:12px;color:#5a5a5a;font-size:26px;font-weight:700;white-space:nowrap}
.foot-brand i{width:36px;height:36px;border-radius:50%;background:#3a3a3a;flex-shrink:0}
.bottom-bar{left:0;top:2349px;width:1200px;height:45px;background:#111;color:#ddd;font-size:13px}
.copyright{left:91px;top:14px}
.pay-cards{left:550px;top:11px;display:flex;gap:6px}
.pay-cards b{width:32px;height:22px;background:#e6e6e6;border-radius:2px}
.follow{left:880px;top:10px;display:flex;gap:9px;align-items:center;font-weight:700;font-size:14px}
.follow i{width:24px;height:24px;border-radius:50%;background:#888}
</style>
</head>
<body>

<div class="abs utility-bar">
  <span><i></i>Sell On Crestwave Glow LED</span>
  <span><i></i>ENG</span>
  <span><i></i>Wish List</span>
  <span><i></i>Sign in</span>
  <span><i></i>My Account</span>
  <span><i></i>Checkout</span>
  <span><i></i>Shopping Cart</span>
</div>

<header class="abs site-header"></header>
<div class="abs brand"><span class="brand-dot"></span>Crestwave Glow LED</div>
<nav class="abs main-nav">
  <a href="#">Home</a><a href="#">About Us</a><a href="#">Products For Sale</a><a href="#">Products For Rental</a><a href="#">Contact Us</a>
</nav>
<div class="abs cart">
  <div class="cart-icon"><svg width="18" height="14" viewBox="0 0 18 14"><path d="M1 4h16l-2 9H3z" fill="#111"/><path d="M5 4l4-3 4 3" stroke="#111" fill="none" stroke-width="1.5"/></svg></div>
  <div class="cart-label">CART <small>(empty)</small></div>
</div>

<section class="abs hero" role="img" aria-label="Video loop of a busy city square lined with bright LED billboards"></section>
<svg class="abs hero-play" width="90" height="90" viewBox="0 0 90 90"><circle cx="45" cy="45" r="41" fill="none" stroke="#fff" stroke-width="4"/><path d="M36 28l26 17-26 17z" fill="#fff"/></svg>
<h1 class="abs hero-title">Lorem ipsum dolor sit amet consectetur adipiscing elit</h1>

<div class="abs how-band"></div>
<div class="abs how-tab"></div>
<div class="abs how-title">How It Works</div>
<div class="abs how-sub">It's As Easy As 1,2,3</div>
<div class="abs step" style="left:290px">
  <div class="step-icon"><svg width="22" height="22" viewBox="0 0 22 22"><circle cx="9" cy="9" r="6" stroke="#111" stroke-width="3" fill="none"/><path d="M13 13l7 7" stroke="#111" stroke-width="3"/></svg></div>
  <div><h4>BROWSE PRODUCTS</h4><p>Find Best Products For Your Needs</p></div>
</div>
<div class="abs step" style="left:590px">
  <div class="step-icon"><svg width="20" height="26" viewBox="0 0 20 26"><path d="M7 2h3v11h2V9h3v4h2v10H5l-4-8 3-1 3 4z" fill="#111"/></svg></div>
  <div><h4>SELECT FOR RENT/BUY</h4><p>Get The Best Deal And Choose</p></div>
</div>
<div class="abs step" style="left:865px">
  <div class="step-icon"><svg width="26" height="20" viewBox="0 0 26 20"><path d="M2 4h14v11H2zM16 8h5l3 4v3h-8z" fill="#111"/><circle cx="7" cy="16" r="2.5" fill="#111"/><circle cx="20" cy="16" r="2.5" fill="#111"/></svg></div>
  <div><h4>DELIVERED / INSTALLED</h4><p>We Get It Delivered To You Or<br>Installed Per Your Choice.</p></div>
</div>

<h2 class="abs section-title" style="top:699px">OUR LED BILLBOARD COMPANY &nbsp;<em>BUSINESS / SELLS</em></h2>
<div class="abs title-rule" style="left:490px;top:736px;width:220px"></div>
<div class="abs pager" style="left:580px;top:732px"><b><svg width="8" height="8"><path d="M6 0L1 4l5 4" stroke="#fff" fill="none"/></svg></b><b><svg width="8" height="8"><path d="M2 0l5 4-5 4" stroke="#fff" fill="none"/></svg></b></div>
<p class="abs section-lead" style="top:758px">Lorem ipsum dolor sit amet, consectetuer adipiscing elit, sed diam nonummy nibh euismod tincidunt ut laoreet dolore magna aliquam.</p>

<div class="abs category" style="left:91px;background:linear-gradient(160deg,#8a3a2a,#3a2a2c 55%,#2a2a2a)" role="img" aria-label="LED billboard at night"><span class="name">LED Billboards</span><span class="mode">Sales &amp; Rental</span></div>
<div class="abs category" style="left:349px;background:linear-gradient(160deg,#5a5e66,#25272d 60%,#1a1b20)" role="img" aria-label="Lit gas station canopy"><span class="name">LED Gas Station lights</span><span class="mode">Sales</span></div>
<div class="abs category" style="left:607px;background:linear-gradient(160deg,#9a2a6c,#4a1240 55%,#2a0f30)" role="img" aria-label="Stage truss with lights"><span class="name">Truss Systems</span><span class="mode">Sales &amp; Rental</span></div>
<div class="abs category" style="left:865px;background:linear-gradient(160deg,#4f8090,#2e4a55 55%,#6a3a5a)" role="img" aria-label="Concert sound system"><span class="name">Sound Systems</span><span class="mode">Sales &amp; Rental</span></div>

<section class="abs panel" style="top:962px;height:478px"></section>
<h2 class="abs section-title" style="top:984px">TOP <em>DEALS</em></h2>
<div class="abs title-rule" style="left:538px;top:1020px;width:124px"></div>
<div class="abs pager" style="left:584px;top:1016px"><b><svg width="8" height="8"><path d="M6 0L1 4l5 4" stroke="#fff" fill="none"/></svg></b><b><svg width="8" height="8"><path d="M2 0l5 4-5 4" stroke="#fff" fill="none"/></svg></b></div>
<p class="abs section-lead" style="top:1044px">Lorem ipsum dolor sit amet, consectetuer adipiscing elit, sed diam nonummy nibh euismod tincidunt ut laoreet dolore magna aliquam.</p>

<article class="abs product" style="left:101px;top:1077px"><div class="thumb" role="img" aria-label="LED billboard on a pole showing a football match" style="background:radial-gradient(ellipse 120px 90px at 50% 42%,#4f8a3a,#2e3a2e 60%,#f4f5f3 100%)"></div><div class="label">LED Billboards</div><div class="actions"><span class="btn btn-buy">Buy Now</span><span class="btn btn-rent">Rent Now</span></div></article>
<article class="abs product" style="left:356px;top:1077px"><div class="thumb" role="img" aria-label="LED flood light fixture" style="background:radial-gradient(ellipse 110px 90px at 50% 40%,#c4c6c8,#8e9194 55%,#f6f6f6 100%)"></div><div class="more"><i>i</i>More Info</div><div class="label">LED Gas Station lights</div><div class="actions"><span class="btn btn-buy">Buy Now</span><span class="btn btn-rent">Rent Now</span></div></article>
<article class="abs product" style="left:611px;top:1077px"><div class="thumb" role="img" aria-label="Truss stand with star curtain" style="background:radial-gradient(ellipse 110px 100px at 50% 45%,#1a1a22,#3a3a44 55%,#f6f6f6 100%)"></div><div class="label">Truss Systems</div><div class="actions"><span class="btn btn-buy">Buy Now</span><span class="btn btn-rent">Rent Now</span></div></article>
<article class="abs product" style="left:868px;top:1077px"><div class="thumb" role="img" aria-label="Portable speaker with colour lights" style="background:radial-gradient(ellipse 90px 110px at 50% 45%,#d8453a,#c9a87a 55%,#f6f4f0 100%)"></div><div class="label">Sound Systems</div><div class="actions"><span class="btn btn-buy">Buy Now</span><span class="btn btn-rent">Rent Now</span></div></article>

<div class="abs perks"></div>
<div class="abs perk-active"></div>
<div class="abs perk" style="left:158px">
  <svg width="34" height="24" viewBox="0 0 34 24"><path d="M2 3h20v14H2zM22 8h6l4 5v4H22z" fill="var(--pink)"/><circle cx="9" cy="19" r="3.5" fill="var(--pink)"/><circle cx="26" cy="19" r="3.5" fill="var(--pink)"/></svg>
  <div><h5>FREE SHIPPING</h5><p>On order over $299.00</p></div>
</div>
<div class="abs perk" style="left:460px">
  <svg width="30" height="28" viewBox="0 0 30 28"><rect x="2" y="9" width="26" height="7" fill="var(--pink)"/><rect x="4" y="16" width="22" height="11" fill="var(--pink)"/><rect x="13" y="9" width="4" height="18" fill="var(--yellow)"/><path d="M15 9c-4-8-10-5-6 0M15 9c4-8 10-5 6 0" stroke="var(--pink)" stroke-width="2" fill="none"/></svg>
  <div><h5>DISCOUNT ON ORDERS</h5><p>Crestwave Glow LED consequat odio sed.</p></div>
</div>
<div class="abs perk" style="left:812px">
  <svg width="28" height="30" viewBox="0 0 28 30"><circle cx="14" cy="9" r="7" fill="var(--pink)"/><path d="M2 29c0-8 5-12 12-12s12 4 12 12z" fill="var(--pink)"/></svg>
  <div><h5>NEED ON HELP</h5><p>On order over $111.00 any Time</p></div>
</div>

<section class="abs panel" style="top:1596px;height:507px"></section>
<div class="abs tabs"><div class="tab tab-active">FEATURED</div><div class="tab">RENTAL</div></div>
<p class="abs section-lead" style="top:1669px">Lorem ipsum dolor sit amet, consectetuer adipiscing elit, sed diam nonummy nibh euismod tincidunt ut laoreet dolore magna aliquam.</p>

<article class="abs product" style="left:101px;top:1703px"><div class="thumb" role="img" aria-label="LED display cabinet showing a nature scene" style="background:radial-gradient(ellipse 120px 100px at 55% 45%,#c87a1e,#5e9a34 55%,#f4f6f0 100%)"></div><div class="more"><i>i</i>More Info</div><div class="label">Lorem ipsum dolor sit amet</div><div class="actions"><span class="btn btn-buy">Buy Now</span><span class="btn btn-rent">Rent Now</span></div></article>
<article class="abs product" style="left:356px;top:1703px"><div class="thumb" role="img" aria-label="Multi lens LED flood light" style="background:radial-gradient(ellipse 110px 95px at 50% 45%,#dfe4ea,#9aa4ae 55%,#f6f7f8 100%)"></div><div class="label">Lorem ipsum dolor sit amet</div><div class="actions"><span class="btn btn-buy">Buy Now</span><span class="btn btn-rent">Rent Now</span></div></article>
<article class="abs product" style="left:611px;top:1703px"><div class="thumb" role="img" aria-label="Aluminium truss sections and stands" style="background:radial-gradient(ellipse 110px 110px at 50% 45%,#a8a8a8,#cfcfcf 55%,#f7f7f7 100%)"></div><div class="label">Lorem ipsum dolor sit amet</div><div class="actions"><span class="btn btn-buy">Buy Now</span><span class="btn btn-rent">Rent Now</span></div></article>
<article class="abs product" style="left:868px;top:1703px"><div class="thumb" role="img" aria-label="Tall party speaker with lit woofers" style="background:radial-gradient(ellipse 70px 120px at 50% 45%,#2f5fa8,#1f2a44 60%,#f4f5f8 100%)"></div><div class="label">Lorem ipsum dolor sit amet</div><div class="actions"><span class="btn btn-buy">Buy Now</span><span class="btn btn-rent">Rent Now</span></div></article>

<div class="abs pager" style="left:584px;top:2060px"><b><svg width="8" height="8"><path d="M6 0L1 4l5 4" stroke="#fff" fill="none"/></svg></b><b><svg width="8" height="8"><path d="M2 0l5 4-5 4" stroke="#fff" fill="none"/></svg></b></div>

<footer class="abs footer"></footer>
<div class="abs quick-links">
  <h6 class="foot-title">Quick Links</h6>
  <ul><li>Home</li><li>About Us</li><li>Products For Sale</li><li>Products For Rental</li><li>Contact Us</li></ul>
</div>
<div class="abs foot-divider" style="left:282px"></div>
<h6 class="abs foot-title" style="left:342px;top:2154px">Contact Details</h6>
<div class="abs map" role="img" aria-label="Map showing the company location"></div>
<div class="abs contact">
  <div class="row"><svg width="10" height="14" viewBox="0 0 10 14"><path d="M5 0a5 5 0 0 1 5 5c0 4-5 9-5 9S0 9 0 5a5 5 0 0 1 5-5z" fill="var(--pink)"/><circle cx="5" cy="5" r="2" fill="#000"/></svg><div><b>Crestwave Glow LED</b><br>16 Lorem ipsum dolor sit sed<br>benetion. Street no-123456</div></div>
  <div class="row"><svg width="11" height="11" viewBox="0 0 11 11"><path d="M1 1h3l1 3-2 1a6 6 0 0 0 3 3l1-2 3 1v3C5 10 1 6 1 1z" fill="var(--pink)"/></svg><div>123-456-7890</div></div>
  <div class="row"><svg width="12" height="9" viewBox="0 0 12 9"><rect width="12" height="9" fill="var(--pink)"/><path d="M0 0l6 5 6-5" stroke="#000" fill="none"/></svg><div>info@crestwaveglowled.com</div></div>
</div>
<div class="abs foot-divider" style="left:800px"></div>
<div class="abs foot-brand"><i></i>Crestwave Glow LED</div>

<div class="abs bottom-bar">
  <div class="abs copyright">Copyright © 2016 Crestwave Glow LED. &nbsp;All Rights Reserved.</div>
  <div class="abs pay-cards"><b></b><b></b><b></b><b></b><b></b></div>
  <div class="abs follow">FOLLOW US: <i></i><i></i><i></i><i></i></div>
</div>

</body>
</html>
```